" Consultorio Médico na área de Nutrologia Pediatrica. Atendimento de crianças e adolescentes (juntamente com seus pais/ou familiar) que precisam orientações de saude relacionados com a alimentação. Avaliação médica da criança, sua alimentação, atividades, rotina, composição corporal e exames laboratoriais para diagnostico e tratamento das suas necessidades especificas para propiciar um crescimento e desenvolvimento saudaveis. Importante: nao é um serviço de nutriçao. É um serviço medico que ingloba outros ambitos de vida do paciente alem do foco principal que é a alimentação, mas tambem habitos de vida, doenças cronicas, sindromes, condiçoes de saude, rotinas, habitos de sono, etc. "

```html
<!DOCTYPE html>
<html lang="pt-BR">
<head>
<meta charset="UTF-8">
<title>NutriPeque – Capa</title>
<link href="https://fonts.googleapis.com/css2?family=Montserrat:wght@400;600&display=swap" rel="stylesheet">
<style>
  :root {
    --page: #ffffff;
    --teal-deep: #2c6470;
    --teal-mid: #3f8a86;
    --mint: #5fae92;
    --mint-light: #86c9a6;
    --text-light: #ffffff;
    --photo-warm: #b98a6a;
    --photo-orange: #d98a3a;
  }
  * { margin: 0; padding: 0; box-sizing: border-box; }
  html, body {
    width: 1200px;
    height: 1200px;
    overflow: hidden;
    background: var(--page);
    font-family: "Montserrat", sans-serif;
  }
  .cover {
    position: absolute;
    left: 0;
    top: 372px;
    width: 1200px;
    height: 456px;
    overflow: hidden;
    background:
      radial-gradient(ellipse 700px 420px at 1050px 40px, var(--mint-light) 0%, transparent 70%),
      linear-gradient(90deg, var(--teal-deep) 0%, var(--teal-mid) 45%, var(--mint) 100%);
  }
  .cover-photo {
    position: absolute;
    left: 0;
    top: 0;
    width: 640px;
    height: 456px;
    background:
      radial-gradient(ellipse 170px 130px at 420px 330px, var(--photo-orange) 0%, transparent 75%),
      radial-gradient(ellipse 260px 220px at 300px 170px, var(--photo-warm) 0%, transparent 75%),
      linear-gradient(90deg, rgba(44,100,112,0.2) 0%, rgba(63,138,134,0) 100%);
    -webkit-mask-image: linear-gradient(90deg, #000 55%, transparent 100%);
    mask-image: linear-gradient(90deg, #000 55%, transparent 100%);
    opacity: 0.85;
  }
  .cover-curves {
    position: absolute;
    inset: 0;
  }
  .brand {
    position: absolute;
    left: 660px;
    top: 100px;
    display: flex;
    align-items: center;
    gap: 22px;
  }
  .brand-mark {
    width: 110px;
    height: 110px;
    border-radius: 50%;
    background: rgba(255,255,255,0.22);
  }
  .brand-name {
    color: var(--text-light);
    font-weight: 600;
    font-size: 60px;
    letter-spacing: -0.5px;
  }
  .website {
    position: absolute;
    left: 773px;
    top: 278px;
    color: var(--text-light);
    font-size: 27px;
    font-weight: 400;
    letter-spacing: 0.5px;
  }
  .social {
    position: absolute;
    left: 850px;
    top: 338px;
    width: 94px;
    display: flex;
    flex-direction: column;
    align-items: center;
    gap: 8px;
  }
  .social-icons { display: flex; gap: 14px; }
  .social-icon {
    width: 38px;
    height: 38px;
    border-radius: 50%;
    border: 2px solid var(--text-light);
    background: rgba(255,255,255,0.15);
  }
  .social-handle {
    color: var(--text-light);
    font-size: 11px;
    font-weight: 600;
    letter-spacing: 0.5px;
  }
</style>
</head>
<body>
  <section class="cover">
    <div class="cover-photo" role="img" aria-label="Criança sorridente segurando laranjas, em tons quentes que se fundem ao fundo verde"></div>
    <svg class="cover-curves" width="1200" height="456" viewBox="0 0 1200 456" aria-hidden="true">
      <path d="M0 300 C 300 200, 700 140, 1200 180" fill="none" stroke="rgba(255,255,255,0.18)" stroke-width="3"/>
      <path d="M380 456 C 500 260, 760 90, 1200 40" fill="none" stroke="rgba(255,255,255,0.12)" stroke-width="60"/>
      <path d="M560 0 C 600 80, 560 180, 480 260" fill="none" stroke="rgba(255,255,255,0.2)" stroke-width="2"/>
      <path d="M0 456 C 200 360, 420 340, 620 400" fill="none" stroke="rgba(20,70,80,0.35)" stroke-width="50"/>
    </svg>
    <div class="brand">
      <div class="brand-mark"></div>
      <div class="brand-name">NutriPeque</div>
    </div>
    <div class="website">www.nutripeque.com.br</div>
    <div class="social">
      <div class="social-icons">
        <span class="social-icon"></span>
        <span class="social-icon"></span>
      </div>
      <div class="social-handle">NUTRIPEQUE</div>
    </div>
  </section>
</body>
</html>
```